Exciting, Bold and Modern Landscaping & Turf care company business card

Hello, I own a lawn and landscaping company in Virginia, USA. We would like to design a bold, dynamic, modern business card that really makes us stand out. I tire of all green business cards with crappy, cartoonish clipart grass on them. It needs to be two sided, on one side i need to highlight our turf care division called "Promised Brighter Meadow" We maintain grass, fertilize it, weed control, etc.. We have a green thumbed gopher as our logo that i will attach. I am looking for something, clean and neat but out of the box in style. Im open to all ideas, and would like different options for them. On the other side, i want to highlight our landscaping division "Quiet Harbor Landscaping" In this division we design and install landscapes. Feel free to visit our website for more info or email me with ANY questions. Our busines cards in the past have highlighted our different services, but i don't want to this time. By the time I hand out a business card we are usually already estimating a project and they know what services we offer. I do want them to look at my card and say "wow thats pretty cool" and for them to think "These guys are something different, not just your standard dirt diggers" The logo doesnt have to be on both sides, but it needs to be on the turf care side. Our phone number and website should also be on at least on side, but need not be on both. The phone number is (555)618-4072 as well as the web address as www.MossbrookYardWorks.example. I like for the web address to have caps like that becasue it makes the long address much easier to read. I would like it in full color, printing costs are not my major concern. I also love rounded corners or interesting die cut designs as well, so feel free to wow me. Whether it be a clean white background with a bold photo to an all black card with a gray logo except for his green thumb with silver foil lettering to anything in between, lets go for it. That bieng said i dont want anything cartoonish, we are still a professional service and i want that to come through. THANKS!
Updates
Project Deadline Extended
Reason: changed project to a committed payment. I would like designers to re-evaluate their interest now and give them extra time to submit designs. Thank you.
we have changed our status to a commited payment to entice more submissions. thank you all for your hard work!
Industry/Entity Type
Professional Service
Look and feel
Each slider illustrates characteristics of the customer's brand and the style your logo design should communicate.

```html
<!DOCTYPE html>
<html lang="en">
<head>
<meta charset="utf-8">
<title>Quiet Harbor Landscaping – Business Card</title>
<link href="https://fonts.googleapis.com/css2?family=Ubuntu:wght@400;500&display=swap" rel="stylesheet">
<style>
  :root {
    --backdrop: #141414;
    --card-light: #7a7a7a;
    --card-mid: #636363;
    --card-dark: #4e4e4e;
    --panel: #ffffff;
    --brand-green: #2f5e34;
    --text-dark: #3a3a3a;
    --mascot-orange: #d9792b;
    --mascot-light: #f0a65a;
    --grass-green: #5a9a2c;
  }
  * { margin: 0; padding: 0; box-sizing: border-box; }
  html, body {
    width: 1200px;
    height: 900px;
    overflow: hidden;
    background: var(--backdrop);
    font-family: "Ubuntu", "Segoe UI", sans-serif;
  }
  .business-card {
    position: absolute;
    left: 84px;
    top: 160px;
    width: 1030px;
    height: 576px;
    border-radius: 26px;
    background: linear-gradient(180deg, var(--card-light) 0%, var(--card-mid) 45%, var(--card-dark) 100%);
    overflow: hidden;
  }
  .name-panel, .contact-panel {
    position: absolute;
    left: 0;
    width: 576px;
    background: var(--panel);
    border-radius: 0 10px 10px 0;
  }
  .name-panel {
    top: 90px;
    height: 96px;
    display: flex;
    align-items: center;
    justify-content: center;
  }
  .company-name {
    font-size: 39px;
    font-weight: 400;
    color: var(--brand-green);
    letter-spacing: 0.3px;
  }
  .contact-panel {
    top: 226px;
    height: 260px;
    text-align: center;
    color: var(--text-dark);
  }
  .phone {
    position: absolute;
    top: 22px;
    left: 0;
    right: 0;
    display: flex;
    align-items: center;
    justify-content: center;
    gap: 12px;
    font-size: 28px;
  }
  .phone-icon { width: 40px; height: 40px; }
  .address {
    position: absolute;
    top: 100px;
    left: 0;
    right: 0;
    font-size: 27px;
    line-height: 36px;
  }
  .website {
    position: absolute;
    top: 206px;
    left: 0;
    right: 0;
    font-size: 31px;
    color: var(--brand-green);
  }
  .mascot-art {
    position: absolute;
    left: 626px;
    top: 90px;
    width: 340px;
    height: 420px;
    border-radius: 48% 48% 12% 12%;
    background:
      linear-gradient(180deg, transparent 82%, var(--grass-green) 82%),
      radial-gradient(ellipse at 55% 40%, var(--mascot-light) 0%, var(--mascot-orange) 70%);
  }
</style>
</head>
<body>
  <main class="business-card">
    <div class="name-panel">
      <h1 class="company-name">Quiet Harbor Landscaping</h1>
    </div>
    <div class="contact-panel">
      <p class="phone">
        <svg class="phone-icon" viewBox="0 0 40 40" aria-hidden="true">
          <circle cx="20" cy="20" r="18" fill="none" stroke="var(--brand-green)" stroke-width="3"/>
          <path d="M13 11c1-1 3-1 4 0l2 3c1 1 0 2-1 3l-1 1c1 3 3 5 6 6l1-1c1-1 2-2 3-1l3 2c1 1 1 3 0 4-2 2-4 3-7 1-5-3-9-7-11-12-1-3 0-5 1-6z" fill="var(--brand-green)"/>
        </svg>
        <span>(555) 618-4072</span>
      </p>
      <p class="address">4817-209 Linden Ct. Suite 118<br>Harbor Falls, VA 23999</p>
      <p class="website">www.MossbrookYardWorks.example</p>
    </div>
    <div class="mascot-art" role="img" aria-label="Company mascot illustration: a cartoon gopher giving a green thumbs-up while standing in a tuft of grass"></div>
  </main>
</body>
</html>
```